Vantage Forge needs a powerpoint design

We need a powerpoint design for an Information Technology based in Fairfax call "Vantage Forge". We are Information Technology solutions provider for the Federal Government. We develop Kestrel, Mobile and Cloud based solutions. We support the Healthcare and Financial sectors of the Government. We would like to see designs that use the colors of our logo. We've attached a copy of our logo. The final design should communicate Information Technology and System Integration with Agile Development.

Target Market(s)

Our target market is the Federal Government and System Integators in the Washington DC area.

Industry/Entity Type

Government

Requirements
Must have
• The powerpoint design must have a professional look.

```html
<!DOCTYPE html>
<html lang="en">
<head>
<meta charset="utf-8">
<title>Vantage Forge – Project Title</title>
<link rel="stylesheet" href="https://fonts.googleapis.com/css2?family=Lato:wght@400;700&family=Tinos&display=swap">
<style>
  :root {
    --navy: #2b3990;
    --navy-deep: #1f2c7a;
    --blue-bright: #0a3ff0;
    --blue-mid: #1d4fe0;
    --blue-glow: #3d7cff;
    --swoosh: #3a5de6;
    --white: #ffffff;
    --ink: #111111;
  }
  html, body {
    margin: 0;
    padding: 0;
    overflow: hidden;
    background: #ffffff;
  }
  .slide {
    position: relative;
    width: 1200px;
    height: 900px;
    overflow: hidden;
    background: var(--white);
  }
  .hero-backdrop {
    position: absolute;
    left: 0;
    top: 0;
    width: 1200px;
    height: 680px;
    background:
      radial-gradient(ellipse 260px 300px at 130px 260px, rgba(90,150,255,0.45), transparent 70%),
      radial-gradient(ellipse 260px 300px at 1070px 230px, rgba(90,160,255,0.45), transparent 70%),
      linear-gradient(90deg, #2f48c4 0%, #1e45dc 25%, var(--blue-bright) 50%, #1e45dc 75%, #2f4ac6 100%);
  }
  .curves {
    position: absolute;
    left: 0;
    top: 0;
    width: 1200px;
    height: 900px;
  }
  .project-title {
    position: absolute;
    left: 120px;
    top: 648px;
    margin: 0;
    font-family: "Lato", sans-serif;
    font-weight: 400;
    font-variant: small-caps;
    font-size: 54px;
    letter-spacing: 1px;
    color: var(--navy);
    line-height: 1;
  }
  .summary {
    position: absolute;
    left: 120px;
    top: 716px;
    display: grid;
    grid-template-columns: 246px 246px;
    row-gap: 8px;
    margin: 0;
    padding: 0;
    list-style: none;
    font-family: "Tinos", serif;
    font-size: 23px;
    color: var(--ink);
    line-height: 28px;
  }
  .brand {
    position: absolute;
    left: 738px;
    top: 708px;
    display: flex;
    align-items: center;
    gap: 18px;
  }
  .brand-square {
    width: 62px;
    height: 62px;
    background: var(--navy);
  }
  .brand-name {
    font-family: "Lato", sans-serif;
    font-weight: 700;
    font-size: 46px;
    color: var(--navy);
    line-height: 1;
  }
</style>
</head>
<body>
  <main class="slide">
    <div class="hero-backdrop" role="img" aria-label="Blue digital backdrop of glowing binary code columns"></div>

    <svg class="curves" viewBox="0 0 1200 900" xmlns="http://www.w3.org/2000/svg" aria-hidden="true">
      <defs>
        <linearGradient id="footerBand" x1="0" y1="0" x2="1" y2="0">
          <stop offset="0" stop-color="#2b3990"/>
          <stop offset="0.5" stop-color="#0a3ff0"/>
          <stop offset="1" stop-color="#2b3990"/>
        </linearGradient>
      </defs>
      <path class="navy-swoosh" d="M0,610 Q520,470 1200,510 L1200,900 L0,900 Z" fill="var(--navy)"/>
      <path class="light-swoosh" d="M260,565 Q640,495 960,590 Q640,512 260,565 Z" fill="var(--swoosh)" stroke="var(--swoosh)" stroke-width="4"/>
      <path class="white-field" d="M0,640 Q420,520 760,535 Q1030,550 1200,625 L1200,900 L0,900 Z" fill="var(--white)"/>
      <rect class="footer-band" x="0" y="867" width="1200" height="33" fill="url(#footerBand)"/>
    </svg>

    <h1 class="project-title">Project Title here</h1>
    <ul class="summary">
      <li>Lorem ipsum dolor sit</li>
      <li>Lorem ipsum dolor sit</li>
      <li>Lorem ipsum dolor sit</li>
      <li>Lorem ipsum dolor sit</li>
      <li>Lorem ipsum dolor sit</li>
    </ul>

    <div class="brand">
      <span class="brand-square"></span>
      <span class="brand-name">Vantage Forge</span>
    </div>
  </main>
</body>
</html>
```